Web Design Project

We are an IT System Integrator. We provide Norvik 500 ERP System, CRM etc. We also provide hardware, networking servicing. Please look at www.brinquot.com.sg. They provide the same service as us. We like to redesign our web site. I will attached the color that I prefer for reference.

Our website is www.ravdu.com.sg.  It has been created about 14 years ago.  We are trying to revamp it with a new look and information.   The new website must be informative, fast.    I have attached an attachment which show the color that I prefer(brownish golden).   

Our competitor (www.brinquot.com) is carrying the same trade as us.  They have all the informations In their website that we will like to have.  Therefore I recommend you to take a look at my competitor website and have a better   
understanding on the kind of information I would like to have for my new website.

This project is guarantee to the person with the best design.  We can have it guarantee.

Target Market(s)

Corporate and companies

Industry/Entity Type

Hardware

```html
<!DOCTYPE html>
<html lang="en">
<head>
<meta charset="utf-8">
<title>Ravdu Information System</title>
<link href="https://fonts.googleapis.com/css2?family=Source+Sans+3:wght@400;600;700&display=swap" rel="stylesheet">
<style>
:root{
  --gold:#a07a35;
  --gold-dark:#8a6528;
  --gold-light:#c9a96a;
  --gold-text:#8b6424;
  --field:#eed9a0;
  --orange:#c9761c;
  --ink:#3a3a3a;
  --muted:#777;
  --panel:#f2f2f2;
  --line:#d8d8d8;
}
*{box-sizing:border-box;margin:0;padding:0}
html,body{width:1200px;height:1100px;overflow:hidden;background:#fff}
body{font-family:"Source Sans 3",sans-serif;color:var(--ink);position:relative}
.abs{position:absolute}
.top-band{left:0;top:0;width:1200px;height:10px;background:var(--gold-light);border-bottom:6px solid var(--gold)}
.hero-bg{left:0;top:99px;width:1200px;height:463px;background:linear-gradient(90deg,#cfcfcf,#fafafa 25%,#fafafa 75%,#cfcfcf)}
.nav{left:0;top:55px;width:1200px;height:44px;background:var(--gold)}
.nav a{position:absolute;top:15px;color:#fbe9b8;font-size:13px;font-weight:600;letter-spacing:.3px;text-decoration:none}
.brand-name{left:467px;top:52px;width:266px;text-align:center;font-size:52px;font-weight:700;color:var(--gold);line-height:1}
.brand-mark{left:660px;top:32px;width:22px;height:22px;border-radius:50%;background:var(--gold-light)}
.brand-tag{left:467px;top:114px;width:266px;text-align:center;font-size:14px;font-weight:600;color:var(--gold-text)}
.hero{left:0;top:0;width:1200px;height:560px}
.quote{left:770px;top:178px;width:263px;height:270px;background:linear-gradient(135deg,#e8d6a8,#b89450 60%,#a8843f);box-shadow:0 3px 6px rgba(0,0,0,.35)}
.quote h2{position:absolute;left:16px;top:12px;font-size:19px;line-height:24px;font-weight:700;color:#fff;letter-spacing:.3px;text-shadow:0 1px 1px rgba(0,0,0,.3)}
.quote label{position:absolute;left:16px;font-size:14px;line-height:18px;color:#2e2a20}
.quote .field{position:absolute;left:16px;width:225px;height:33px;background:var(--field);border:1px solid #b99548;border-radius:3px}
.quote .send{position:absolute;left:150px;top:229px;width:90px;height:29px;border-radius:3px;background:linear-gradient(#d98a2a,#b8661a);color:#fff;font-size:13px;font-weight:600;text-align:center;line-height:29px}
.gold-band{left:0;top:562px;width:1200px;height:8px;background:var(--gold)}
.partners{left:0;top:570px;width:1200px;height:75px;background:var(--panel);border-bottom:1px solid var(--line)}
.partners h3{position:absolute;left:130px;top:25px;font-size:18px;font-weight:700;color:#333}
.badge{position:absolute;top:20px;height:40px;background:#dcdcdc;border-radius:4px}
.search{position:absolute;left:850px;top:21px;width:220px;height:35px;border:1px solid #cbcbcb;background:#fff;border-radius:3px}
.search span{position:absolute;left:12px;top:8px;font-size:13px;font-style:italic;color:#999}
.search .btn{position:absolute;right:-1px;top:-1px;width:41px;height:35px;background:linear-gradient(#c7a764,#9c7a37);border-radius:0 3px 3px 0}
.card{top:660px;width:220px;height:238px;background:var(--gold)}
.card h4{position:absolute;left:39px;top:10px;font-size:16px;font-weight:600;color:#fff}
.card .play{position:absolute;left:8px;top:11px;width:19px;height:19px;border-radius:50%;background:#fff}
.card .play::after{content:"";position:absolute;left:7px;top:5px;border-left:7px solid #333;border-top:4.5px solid transparent;border-bottom:4.5px solid transparent}
.card .body{position:absolute;left:7px;top:39px;width:207px;height:238px;background:linear-gradient(#fff,#efefef);box-shadow:0 1px 3px rgba(0,0,0,.25)}
.card .photo{height:106px}
.card p{font-size:13px;line-height:20px;text-align:center;padding:8px 12px 0;color:#333}
.card .more{position:absolute;left:0;bottom:12px;width:100%;text-align:center;font-size:13px;font-weight:600;color:var(--gold-text)}
.footer{left:0;top:963px;width:1200px;height:137px;background:linear-gradient(#ececec,#fff 30px)}
.footer .links{position:absolute;left:131px;top:22px;font-size:13px;color:var(--gold-text)}
.footer .links i{font-style:normal;margin:0 6px}
.footer .copy{position:absolute;left:131px;top:65px;font-size:12px;color:var(--muted);line-height:20px}
.footer .copy b{font-weight:400;color:var(--gold-text)}
.footer .join{position:absolute;left:959px;top:22px;font-size:13px;color:var(--gold-text)}
.social{position:absolute;top:50px;width:30px;height:30px;border-radius:4px}
</style>
</head>
<body>
<div class="abs top-band"></div>
<div class="abs hero-bg"></div>
<nav class="abs nav">
  <a style="left:130px">SOLUTIONS</a>
  <a style="left:240px">HARDWARE</a>
  <a style="left:353px">SERVICES</a>
  <a style="left:777px">CLIENTS</a>
  <a style="left:882px">ABOUT US</a>
  <a style="left:995px">CONTACT US</a>
</nav>

<svg class="abs hero" viewBox="0 0 1200 560">
  <defs>
    <linearGradient id="photo" x1="0" y1="0" x2="1" y2="0">
      <stop offset="0" stop-color="#c8d2dd"/>
      <stop offset=".45" stop-color="#6a6a70"/>
      <stop offset=".7" stop-color="#cfc3b4"/>
      <stop offset="1" stop-color="#e6e8ec"/>
    </linearGradient>
    <linearGradient id="shield" x1="0" y1="0" x2="0" y2="1">
      <stop offset="0" stop-color="#f4f4f4"/>
      <stop offset="1" stop-color="#ffffff"/>
    </linearGradient>
  </defs>
  <ellipse cx="600" cy="530" rx="460" ry="10" fill="rgba(0,0,0,.12)"/>
  <path d="M130,100 L130,498 Q600,560 1070,498 L1070,100 Z" fill="#fff"/>
  <path d="M134,102 L134,494 Q600,550 1066,494 L1066,102 Z" fill="url(#photo)" role="img" aria-label="Photo of business people reviewing a chart at a meeting"/>
  <circle cx="156" cy="480" r="8" fill="#d4951f"/>
  <circle cx="178" cy="480" r="8" fill="#9b8a4a"/>
  <circle cx="202" cy="480" r="8" fill="#9b8a4a"/>
  <circle cx="227" cy="480" r="8" fill="#9b8a4a"/>
  <path d="M467,15 L733,15 L733,115 L600,187 L467,115 Z" fill="url(#shield)" stroke="#d9d9d9" stroke-width="2"/>
</svg>
<div class="abs brand-name">ravdu</div>
<div class="abs brand-mark"></div>
<div class="abs brand-tag">Ravdu Information System</div>

<form class="abs quote">
  <h2>GET A QUOTE NOW !</h2>
  <label style="top:46px">Name</label><div class="field" style="top:66px"></div>
  <label style="top:106px">Email Address</label><div class="field" style="top:126px"></div>
  <label style="top:163px">Contact No.</label><div class="field" style="top:183px"></div>
  <div class="send">SEND NOW</div>
</form>

<div class="abs gold-band"></div>
<section class="abs partners">
  <h3>PARTNERS:</h3>
  <div class="badge" style="left:245px;width:45px"></div>
  <div class="badge" style="left:340px;width:92px"></div>
  <div class="badge" style="left:488px;width:102px"></div>
  <div class="badge" style="left:650px;width:70px"></div>
  <div class="badge" style="left:772px;width:42px;border-radius:50%"></div>
  <div class="search"><span>Search...</span>
    <svg class="btn" viewBox="0 0 41 35"><circle cx="18" cy="15" r="6" fill="none" stroke="#fff" stroke-width="2.5"/><line x1="22" y1="19" x2="29" y2="26" stroke="#fff" stroke-width="3.5" stroke-linecap="round"/></svg>
  </div>
</section>

<article class="abs card" style="left:130px">
  <span class="play"></span><h4>Norvik Certified</h4>
  <div class="body">
    <div class="photo" style="background:#00806a" role="img" aria-label="Norvik certification banner"></div>
    <p>Aliquam molestie, mi et imperdiet euismod, dui purus auctor tellus, et interdum lacus lectus et ante.</p>
    <div class="more">LEARN MORE</div>
  </div>
</article>
<article class="abs card" style="left:370px">
  <span class="play"></span><h4>Success Stories</h4>
  <div class="body">
    <div class="photo" style="background:linear-gradient(#e4e8ee,#8a9bb5)" role="img" aria-label="Photo of a group of smiling professionals"></div>
    <p>Aliquam molestie, mi et imperdiet euismod, dui purus auctor tellus, et interdum lacus lectus et ante.</p>
    <div class="more">LEARN MORE</div>
  </div>
</article>
<article class="abs card" style="left:611px">
  <span class="play"></span><h4>Latest Norvik 500</h4>
  <div class="body">
    <div class="photo" style="background:linear-gradient(90deg,#3c3c40,#d8dde6 50%,#505058)" role="img" aria-label="Photo of hands reviewing a printed report chart"></div>
    <p>Aliquam molestie, mi et imperdiet euismod, dui purus auctor tellus, et interdum lacus lectus et ante.</p>
    <div class="more">LEARN MORE</div>
  </div>
</article>
<article class="abs card" style="left:851px">
  <span class="play"></span><h4>Services Beyond</h4>
  <div class="body">
    <div class="photo" style="background:linear-gradient(90deg,#cdd3da,#6d6660 50%,#dfe2e6)" role="img" aria-label="Photo of a team meeting around a laptop"></div>
    <p>Aliquam molestie, mi et imperdiet euismod, dui purus auctor tellus, et interdum lacus lectus et ante.</p>
    <div class="more">LEARN MORE</div>
  </div>
</article>

<footer class="abs footer">
  <div class="links">Log Incident<i>|</i>Enquiry<i>|</i>Site Map</div>
  <div class="copy">Copyright © 2013 <b>Ravdu Information System.</b><br>All Right Reserved</div>
  <div class="join">Join Our Network</div>
  <div class="social" style="left:959px;background:#3b5a9a" aria-label="Social network link"></div>
  <div class="social" style="left:999px;background:#5bc0e4" aria-label="Social network link"></div>
  <div class="social" style="left:1039px;background:#1d78b4" aria-label="Social network link"></div>
</footer>
</body>
</html>
```